Australian Consultant Pharmacist Business Needs A3 Flyer for Medical Centre

Our business has just secured a deal in a medical centre to offer our consulting services. We have installed our software on the doctors computers and would like to have an A3 flyer to put on their walls to remind them about our services and explain very briefly how to use our simple software.

We would like the flyer to be vibrant and very simple whilst conveying our message of improving patient health outcomes and illustrating how to use our software and service.

We provide Home Medicine Reviews (HMR) for General Practitioners (GP) at medical centres.

There are 3 pathways for a GP to use our service, all resulting in the same outcome.

The outcome is the Dr sends us a referral for a HMR for their patient. In turn they receive a report back after we have performed the HMR.

Pathways
1.
-GP Opens Patient File in medical prescribing software
-If patient is eligible for a HMR, an alert will pop up in bottom right hand corner (approx 30 seconds)
- Click Send Referral
- New page opens, select reason for referral ie. several medicines
- Press Send - referral is sent electronically to Pharmacist

2.
No alert pops up but GP still wants to refer.
Right click RX Notify program - RX Notify program is identified by the bell shape icon in the bottom right side of the desktop tray next to the time.
Click refer current patient - this will refer the patient currently open on the GP prescribing software

3. GP would like to send HMR Referal via Fax.
Fax number 03 9172 3408

I have attached some examples of how the software and service works, including screen shots and some power points. I would like to use these as ideas for our A3 Flyer.

Good Luck!

Target Market(s)

Doctors

Industry/Entity Type

Health Service

Colors
f37122
0455a3
3176b5
33a6d7
f68d4c

Requirements
Must have
• Our company name - Brightpath Care HMR
• Our email brightpathcarehmr@mailvista.example
• our fax number
• the 3 ways to use our service and how
• prefer images and short keyword descriptions
• convey idea of improving patient health
• ensure our service comes accross as simple and effecient
Nice to have
• images, vibrant,
Should not have
• lengthy descriptions

```html
<!DOCTYPE html>
<html lang="en">
<head>
<meta charset="utf-8">
<title>Brightpath Care HMR – Flyer</title>
<link rel="stylesheet" href="https://fonts.googleapis.com/css2?family=Oswald:wght@500;600&family=Lato:wght@400;700;900&family=Libre+Baskerville:wght@700&display=swap">
<style>
:root{
  --navy:#0e4a7f;
  --navy-deep:#0a3a68;
  --blue:#0455a3;
  --blue-mid:#3176b5;
  --sky:#33a6d7;
  --orange:#f37122;
  --orange-soft:#f68d4c;
  --grey-light:#eef0f2;
  --grey-mid:#cfd3d7;
  --grey-band:#9a9fa5;
  --white:#ffffff;
}
*{margin:0;padding:0;box-sizing:border-box}
html,body{width:900px;height:1200px;overflow:hidden;background:#f4f4f4}
.flyer{position:relative;width:900px;height:1200px;overflow:hidden;font-family:"Lato",sans-serif;
  background:linear-gradient(180deg,var(--grey-light) 0%,#ffffff 40%,#e6e8ea 100%)}

/* header */
.header{position:absolute;left:0;top:0;width:900px;height:330px;background:var(--navy)}
.header-photo{position:absolute;right:0;top:0;width:520px;height:330px;
  background:linear-gradient(90deg,var(--navy) 0%,rgba(80,140,190,.7) 25%,#a9cde6 55%,#d6e8f3 100%)}
.brand{position:absolute;left:46px;top:36px;font-family:"Oswald",sans-serif;color:var(--orange);text-transform:uppercase;line-height:1}
.brand-main{font-size:74px;font-weight:600;letter-spacing:.5px}
.brand-rule{width:318px;height:3px;background:var(--white);margin:10px 0 10px}
.brand-sub{font-size:46px;font-weight:500;letter-spacing:.5px}
.intro{position:absolute;left:46px;top:210px;width:420px;color:var(--white);font-size:23px;font-weight:700;line-height:1.2}

/* outcome banner */
.outcome{position:absolute;left:0;top:318px;width:900px;height:140px}
.outcome svg{position:absolute;left:0;top:0}
.outcome-text{position:absolute;left:170px;top:12px;width:560px;text-align:center;color:var(--white);font-size:16.5px;line-height:1.15}
.outcome-rule{width:250px;height:2px;background:var(--blue);margin:8px auto 12px}

/* steps */
.step{position:absolute;left:60px;width:770px;display:flex;gap:6px}
.step-body{flex:0 0 600px;background:var(--navy);color:var(--white);border-radius:0 14px 14px 14px;padding:8px 20px;font-size:12px;line-height:1.2;display:flex;flex-direction:column;justify-content:center}
.step-title{font-weight:700;font-size:12.5px;margin-bottom:4px}
.step-body ul{list-style:none}
.step-body li::before{content:"\25CF\00A0"}
.step-body.large{font-size:14px;line-height:1.25}
.step-body.large .step-title{font-size:14px;margin-bottom:6px}
.step-body.compact{font-size:11.5px;line-height:1.2}
.step-shot{flex:1;border:2px solid var(--orange);background:linear-gradient(180deg,#f7f9fb 0%,#dfe6ee 75%,#7fa2c4 100%)}
.step-1{top:472px;height:112px}
.step-2{top:596px;height:96px}
.step-3{top:704px;height:96px}
.step-4{top:812px;height:122px}

/* footer */
.footer{position:absolute;left:0;top:986px;width:900px;height:214px;background:var(--navy-deep)}
.footer-curve{position:absolute;left:0;top:960px}
.tagline{position:absolute;left:0;top:1012px;width:432px;height:62px;background:var(--orange);border-radius:0 10px 10px 0;
  color:var(--white);font-family:"Libre Baskerville",serif;font-weight:700;font-size:21px;line-height:1.05;padding:8px 0 0 78px}
.contact{position:absolute;left:78px;top:1084px;color:var(--white)}
.email{display:flex;align-items:center;gap:8px;font-size:17px;font-weight:700}
.fax-label{font-size:17px;font-weight:700;margin-top:14px}
.fax-number{font-size:19px;font-weight:900;color:var(--orange);margin-top:4px;letter-spacing:.5px}
.still-life{position:absolute;left:470px;top:975px;width:430px;height:215px;border-radius:0 0 0 90px;
  background:radial-gradient(ellipse at 40% 30%,#ffffff 0%,#e8eef2 45%,#f2c3a0 70%,#e7e7e7 100%)}
</style>
</head>
<body>
<main class="flyer">

  <header class="header">
    <div class="header-photo" role="img" aria-label="Photo of a pharmacist talking with an elderly couple in a pharmacy"></div>
    <div class="brand">
      <div class="brand-main">Brightpath</div>
      <div class="brand-rule"></div>
      <div class="brand-sub">Care HMR</div>
    </div>
    <p class="intro">We provide Home Medicine Reviews (HMR) for General Practitioners (GP) at medical centres.</p>
  </header>

  <section class="outcome">
    <svg width="900" height="140" viewBox="0 0 900 140" aria-hidden="true">
      <polygon points="0,0 900,0 900,12 0,12" fill="#7e8489"/>
      <polygon points="140,0 760,0 712,136 188,136" fill="#9a9fa5"/>
    </svg>
    <div class="outcome-text">
      <p>There are 3 pathways for a GP to use our service,<br>all resulting in the same outcome.</p>
      <div class="outcome-rule"></div>
      <p>The outcome is the Dr sends us a referral for a HMR for their patient.<br>In turn they receive a report back after we have performed the HMR.</p>
    </div>
  </section>

  <section class="step step-1">
    <div class="step-body">
      <p class="step-title">GP Opens Patient File in medical prescribing software</p>
      <ul>
        <li>If patient is eligible for a HMR, an alert will pop up in bottom right hand corner<br>&nbsp;&nbsp;&nbsp;(approx 30 seconds)</li>
        <li>Click Send Referral</li>
        <li>New page opens, select reason for referral ie. several medicines</li>
        <li>Press Send - referral is sent electronically to Pharmacist</li>
      </ul>
    </div>
    <div class="step-shot" role="img" aria-label="Screenshot of the RX Notify program in the desktop tray"></div>
  </section>

  <section class="step step-2">
    <div class="step-body large">
      <p class="step-title">RX Notify Pop Up</p>
      <p><strong>RX Notify will notify you when an eligible patient file is openedin ClinicDesk.</strong></p>
    </div>
    <div class="step-shot" role="img" aria-label="Screenshot of the RX Notify pop-up window"></div>
  </section>

  <section class="step step-3">
    <div class="step-body large">
      <p class="step-title">Send Referral to Pharmacist.</p>
      <ul>
        <li>This screen will appear after pressing send referral.</li>
        <li>Once you press SEND, no further action is required.</li>
        <li>You may choose to write a note in the patients file that a HMR has been requested.</li>
      </ul>
    </div>
    <div class="step-shot" role="img" aria-label="Screenshot of the send to pharmacist screen"></div>
  </section>

  <section class="step step-4">
    <div class="step-body compact">
      <p class="step-title">4.IF, RX Notify Does Not Pop Up</p>
      <p>&#9679;Patient IS still eligible if you find there is a clinical need</p>
      <p>&#9679;You can still send a referral electronically to Revio if no alert pops up.</p>
      <p>&#9679;1. Open the Patient File in ClinicDesk</p>
      <p>&#9679;2. Right Click on RX Notify Bell Icon.</p>
      <p>&#9679;3.Click refer current patient</p>
      <p>&#9679;4. Send Referal</p>
    </div>
    <div class="step-shot" role="img" aria-label="Screenshot of the refer current patient form"></div>
  </section>

  <footer>
    <svg class="footer-curve" width="900" height="40" viewBox="0 0 900 40" aria-hidden="true">
      <path d="M0 26 H470 V40 H0 Z" fill="#0a3a68"/>
    </svg>
    <div class="footer"></div>
    <div class="still-life" role="img" aria-label="Photo of a glass of water with a pile of colourful pills"></div>
    <div class="tagline">our service comes accross<br>as simple and effecient</div>
    <div class="contact">
      <p class="email">
        <svg width="14" height="10" viewBox="0 0 14 10" aria-hidden="true"><rect width="14" height="10" rx="1" fill="#f37122"/><path d="M0.5 0.8 L7 5.5 L13.5 0.8" stroke="#fff" stroke-width="1.2" fill="none"/></svg>
        brightpathcarehmr@mailvista.example
      </p>
      <p class="fax-label">Fax number:</p>
      <p class="fax-number">03 9172 3408</p>
    </div>
  </footer>

</main>
</body>
</html>
```